The company Velquist needs a design for CBD capsules

We (Velquist) need a new design for our CBD capsules. We already have a design for CBD oil. However, we do not want to use this completely. The Talmbex label and the cans serve as a template. Please upload in the format 139mm x 59mm incl.
2mm bleed all around and in .pdf vector. The logo files for Velquist are included in the briefing.

Industry/Entity Type

Onlineshop

Colors
00AB8E
00BBA5
67D7C9
C6EFE9
E9F9F6

Requirements
Must have
• Please in the format 139mm x 59mm incl. 2mm bleed all around and .pdf vector
Should not have
• It shouldn't be the same label, but it should be recognizable.

```html
<!DOCTYPE html>
<html lang="de">
<head>
<meta charset="utf-8">
<title>Velquist CBD Capsules Label</title>
<link href="https://fonts.googleapis.com/css2?family=Oswald:wght@400;500;700&family=Allura&display=swap" rel="stylesheet">
<style>
  :root {
    --page-bg: #e6e8e8;
    --label-teal: #2f6e77;
    --label-white: #ffffff;
    --ink-teal: #2f6e77;
    --leaf-green: #3f7a3c;
    --leaf-dark: #1f3b22;
  }
  html, body {
    margin: 0;
    width: 1200px;
    height: 1200px;
    overflow: hidden;
    background: var(--page-bg);
  }
  .canvas {
    position: relative;
    width: 1200px;
    height: 1200px;
  }
  .label {
    position: absolute;
    left: 50px;
    top: 367px;
    width: 1100px;
    height: 466px;
    background: var(--label-teal);
    overflow: hidden;
  }
  .label-wave {
    position: absolute;
    inset: 0;
  }
  .brand {
    position: absolute;
    left: 0;
    width: 100%;
    top: 80px;
    text-align: center;
    font-family: "Oswald", sans-serif;
    font-weight: 500;
    font-size: 38px;
    letter-spacing: 1px;
    color: var(--label-white);
    line-height: 1;
  }
  .product-name {
    position: absolute;
    left: 0;
    width: 100%;
    top: 138px;
    text-align: center;
    font-family: "Oswald", sans-serif;
    font-weight: 700;
    font-size: 104px;
    color: var(--label-white);
    line-height: 1;
  }
  .product-type {
    position: absolute;
    left: 0;
    width: 100%;
    top: 240px;
    text-align: center;
    font-family: "Oswald", sans-serif;
    font-weight: 500;
    font-size: 22px;
    letter-spacing: 3px;
    color: var(--label-white);
    line-height: 1;
  }
  .hemp-visual {
    position: absolute;
    left: 598px;
    top: 274px;
    width: 170px;
    height: 140px;
    border-radius: 50% 45% 40% 55%;
    background: radial-gradient(circle at 50% 50%, var(--leaf-dark) 0 28%, var(--leaf-green) 30% 100%);
  }
  .claims {
    position: absolute;
    left: 448px;
    top: 326px;
    margin: 0;
    padding: 0;
    list-style: none;
    font-family: "Oswald", sans-serif;
    font-weight: 400;
    font-size: 13px;
    color: var(--ink-teal);
  }
  .claims li {
    display: flex;
    align-items: center;
    gap: 5px;
    height: 23px;
  }
  .claims svg { width: 11px; height: 11px; }
  .spectrum {
    position: absolute;
    left: 418px;
    top: 388px;
    font-family: "Allura", cursive;
    font-size: 36px;
    color: var(--ink-teal);
    line-height: 1;
  }
  .strength {
    position: absolute;
    left: 728px;
    top: 424px;
    font-family: "Oswald", sans-serif;
    font-weight: 400;
    font-size: 24px;
    color: var(--label-white);
    line-height: 1;
  }
</style>
</head>
<body>
<main class="canvas">
  <section class="label">
    <svg class="label-wave" viewBox="0 0 1100 466" width="1100" height="466" aria-hidden="true">
      <path d="M0 300 C 220 330 420 290 570 300 C 610 305 625 380 640 466 L0 466 Z" fill="var(--label-white)"/>
    </svg>

    <div class="brand">Velquist</div>
    <div class="product-name">CBD</div>
    <div class="product-type">CAPSULES</div>

    <div class="hemp-visual" role="img" aria-label="Hemp leaf with dark softgel capsules"></div>

    <ul class="claims">
      <li><svg viewBox="0 0 12 12"><path d="M1.5 6.5 L4.5 9.5 L10.5 2.5" fill="none" stroke="currentColor" stroke-width="2"/></svg>VEGAN</li>
      <li><svg viewBox="0 0 12 12"><path d="M1.5 6.5 L4.5 9.5 L10.5 2.5" fill="none" stroke="currentColor" stroke-width="2"/></svg>GENTECHNIK FREI</li>
    </ul>

    <div class="spectrum">Vollspektrum</div>
    <div class="strength">10%</div>
  </section>
</main>
</body>
</html>
```